Real estate development company, seeking investors and joint venture partners to fund

i have attached a investor proposal document to attact joint venture money partners to invest in property development. the existing document i have attached need s to be polised to a professional standard and needs to be in word , so i can edit the content on ongoing basis i.e. numbers and photos etc . this document will be updated with new opportunites, propoerties, feasibility edited and emailed to potential investors. This document needs to be Red hot!! Company name Bright meadow collective. All tables, place holders for photos need to be provided so i can easily remove and paste new /updated photos.

Target Market(s)

investors , money partners property developers

Requirements
Must have
• Design to be in word document

Content should be modifyable by me as each project will have unique cost, sales etc

i want to be able to email to my clients

i may also print as required
Nice to have
• Feel free to modify table/images/look and feel

```html
<!DOCTYPE html>
<html lang="en">
<head>
<meta charset="utf-8">
<title>Investor Report – Bright meadow collective</title>
<link href="https://fonts.googleapis.com/css2?family=Roboto+Condensed:wght@400;700&family=Roboto:wght@400;500;700&display=swap" rel="stylesheet">
<style>
:root{
  --orange:#f7923e;
  --orange-line:#f9a35a;
  --ink:#222;
  --muted:#444;
  --panel:#3b3b3b;
  --strip:#f4f4f4;
  --stage:#666;
  --placeholder:#cfcfcf;
}
*{box-sizing:border-box;margin:0;padding:0}
html,body{width:1200px;height:1200px;overflow:hidden}
body{background:var(--stage);font-family:"Roboto",sans-serif;color:var(--ink);position:relative}
.page{position:absolute;width:350px;height:492px;background:#fff;overflow:hidden}
.p1{left:38px;top:78px}.p2{left:425px;top:78px}.p3{left:811px;top:78px}
.p4{left:38px;top:625px}.p5{left:425px;top:625px}.p6{left:811px;top:625px}
.abs{position:absolute}
.header-strip{position:absolute;left:0;top:0;width:100%;height:34px;background:var(--strip);font-size:6.4px;letter-spacing:.1px;color:var(--ink)}
.header-strip span{position:absolute;top:19px}
.header-strip .left{left:29px}.header-strip .right{right:29px}
.page-foot{position:absolute;left:0;bottom:12px;width:100%;height:20px;border-bottom:1px solid var(--orange-line)}
.page-foot .num{position:absolute;left:0;top:0;width:40px;height:20px;background:var(--orange);color:#fff;font-size:7px;padding:6px 0 0 19px}
.section-title{position:absolute;left:29px;top:52px;font-family:"Roboto Condensed",sans-serif;font-weight:700;font-size:31px;color:var(--orange);letter-spacing:.5px;line-height:1}
.title-bar{position:absolute;right:0;height:23px;background:var(--orange)}
.photo{position:absolute}
/* cover */
.logo-box{left:221px;top:14px;width:101px;height:42px;border:1px solid #222;font-size:9.5px;line-height:12px;padding:8px 5px}
.cover-title{left:29px;top:75px;font-family:"Roboto Condensed",sans-serif;font-weight:700;font-size:32px;color:var(--orange);letter-spacing:.5px}
.cover-sub{left:29px;top:112px;font-size:13px;font-weight:500}
.prepared{left:0;top:385px;width:171px;height:76px;background:var(--panel);color:#fff}
.prepared .bar{position:absolute;left:0;top:25px;width:64px;height:13px;background:var(--orange)}
.prepared .label{position:absolute;left:72px;top:15px;font-size:6px}
.prepared .name{position:absolute;left:72px;top:25px;font-size:10px;color:var(--orange)}
.prepared .org{position:absolute;left:72px;top:44px;font-size:6px;line-height:10.5px}
.contact-line{display:flex;align-items:center;gap:6px}
.phone{left:206px;top:425px;font-size:13.5px;font-weight:700}
.email{left:206px;top:451px;font-size:6px}
.icon-dot{width:13px;height:13px;border-radius:50%;background:var(--orange);display:flex;align-items:center;justify-content:center}
/* letter */
.letter{left:31px;top:69px;width:290px;font-size:5.6px;line-height:8.2px;text-align:justify}
.letter p{margin-bottom:14px}
.sign{left:30px;font-size:5.6px}
.photo-slot{left:30px;top:284px;width:103px;height:118px;background:var(--placeholder);display:flex;align-items:center;justify-content:center;font-size:8.5px;font-weight:500}
/* contents */
.toc{left:34px;top:107px;width:287px;list-style:none}
.toc li{display:flex;align-items:baseline;height:27.5px;font-size:8.6px;font-weight:500}
.toc li::before{content:"";width:4px;height:4px;border-radius:50%;background:var(--orange);margin-right:5px;transform:translateY(-1px)}
.toc .dots{flex:1;border-bottom:1px dotted #777;margin:0 5px;transform:translateY(-2px)}
.toc .pg{width:14px;font-weight:400}
/* proposal */
.sub-head{font-size:16px;color:var(--orange)}
.sub-head::after{content:"";display:block;width:16px;height:1.5px;background:var(--orange);margin-top:2px}
.body-small{font-size:6.2px;line-height:10.4px}
/* location */
.chip{left:30px;width:119px;height:18px;background:var(--orange);color:#fff;font-size:6px;padding:6px 0 0 9px}
.overview-head{left:167px;top:290px;font-size:13px;color:var(--orange)}
.overview-lead{left:167px;top:312px;width:160px;font-size:9.2px;font-weight:700;line-height:12px}
.overview-text{left:167px;top:342px;width:160px;font-size:5.8px;line-height:8.3px}
/* photos */
.framed{border:2px solid var(--orange)}
.tab{background:var(--orange);color:#fff;font-size:9px;display:flex;align-items:center;justify-content:center;border-radius:3px}
.tab span{transform:rotate(-90deg);white-space:nowrap}
.pin-text{left:33px;top:206px;font-size:5.8px;line-height:8px}
.map-tag{background:var(--orange);color:#fff;font-family:"Roboto Condensed",sans-serif;font-weight:700;font-size:8px;padding:3px 4px;text-align:center;line-height:9px}
.vertical-label{left:-22px;top:318px;transform:rotate(-90deg);font-family:"Roboto Condensed",sans-serif;font-weight:700;font-size:11.5px;color:var(--orange);white-space:nowrap}
.costs-head{left:55px;top:414px;font-family:"Roboto Condensed",sans-serif;font-weight:700;font-size:9.5px}
.costs-head em{font-style:normal;color:var(--orange)}
.costs{left:55px;top:431px;width:267px;border-collapse:collapse;font-size:5.8px}
.costs td,.costs th{border:1px solid #555;height:12px;padding:0 6px}
.costs th{background:var(--orange);color:#fff;font-weight:500}
.costs th:first-child{background:#fff}
.costs td:not(:first-child){text-align:center}
</style>
</head>
<body>

<!-- Page 1: cover -->
<section class="page p1">
  <div class="abs logo-box">Bright meadow collective</div>
  <h1 class="abs cover-title">INVESTOR REPORT</h1>
  <p class="abs cover-sub">Dual occ development</p>
  <div class="abs prepared">
    <div class="bar"></div>
    <span class="label">Prepared By:</span>
    <span class="name">Daniel Marlowe</span>
    <span class="org">Bright meadow collective<br>ABN</span>
  </div>
  <div class="abs phone contact-line">
    <span class="icon-dot"><svg width="7" height="7" viewBox="0 0 24 24"><path fill="#fff" d="M6.6 10.8a15 15 0 0 0 6.6 6.6l2.2-2.2a1 1 0 0 1 1-.25 11.4 11.4 0 0 0 3.6.57 1 1 0 0 1 1 1V20a1 1 0 0 1-1 1A17 17 0 0 1 3 4a1 1 0 0 1 1-1h3.5a1 1 0 0 1 1 1c0 1.25.2 2.45.57 3.57a1 1 0 0 1-.25 1z"/></svg></span>
    0400-555-012
  </div>
  <div class="abs email contact-line">
    <span class="icon-dot"><svg width="7" height="6" viewBox="0 0 24 18"><rect x="1" y="1" width="22" height="16" rx="2" fill="#fff"/><path d="M2 2l10 8 10-8" stroke="#f7923e" stroke-width="2" fill="none"/></svg></span>
    info@brightmeadowcollective.com.au
  </div>
</section>

<!-- Page 2: letter -->
<section class="page p2">
  <header class="header-strip"><span class="left">PHONE NUMBER</span><span class="right">TRADING NAME</span></header>
  <div class="abs letter">
    <p>Lorem ipsum dolor sit amet, consectetur adipiscing elit, sed do eiusmod tempor incididunt ut labore et dolore magna aliqua. Eget duis at tellus at urna condimentum mattis. Vitae et leo duis ut. Amet consectetur adipiscing elit duis tristique sollicitudin nibh sit amet. Nunc id cursus metus aliquam eleifend mi in nulla posuere. Commodo nulla facilisi nullam vehicula ipsum a arcu cursus vitae. Nunc aliquet bibendum enim facilisis gravida neque convallis a. Rutrum quisque non tellus orci.</p>
    <p>Nisl pretium fusce id velit. Non sodales neque sodales ut. Consectetur adipiscing elit duis tristique sollicitudin nibh sit. Vitae turpis massa sed elementum tempus. Morbi leo urna molestie at. Aenean sed adipiscing diam donec adipiscing tristique risus nec. Lobortis feugiat vivamus at augue eget arcu dictum varius. Turpis massa tincidunt dui ut ornare lectus sit. Id donec ultrices tincidunt arcu non sodales neque sodales ut. Aliquet bibendum enim facilisis gravida.</p>
  </div>
  <span class="abs sign" style="top:320px">&lt;Insert signature&gt;</span>
  <span class="abs sign" style="top:334px">&lt;Insert name&gt;</span>
  <div class="abs photo-slot" style="top:284px;top:284px">&lt;INSERT PHOTO&gt;</div>
  <footer class="page-foot"><span class="num">2</span></footer>
</section>

<!-- Page 3: contents -->
<section class="page p3">
  <header class="header-strip"><span class="left">CREATIVITY AGENCY</span><span class="right">PROPOSAL</span></header>
  <h2 class="section-title">CONTENTS</h2>
  <div class="title-bar" style="left:189px;top:60px"></div>
  <ul class="abs toc">
    <li>PROPOSAL<span class="dots"></span><span class="pg">4</span></li>
    <li>LOCATION<span class="dots"></span><span class="pg">4</span></li>
    <li>PHOTOS<span class="dots"></span><span class="pg">5</span></li>
    <li>FINANCIAL FEASIBILITY<span class="dots"></span><span class="pg">5</span></li>
    <li>CASH FLOW ANALYSIS<span class="dots"></span><span class="pg">6</span></li>
    <li>CAPITAL REQUIREMENTS<span class="dots"></span><span class="pg">7</span></li>
    <li>SUBURB PROFILE<span class="dots"></span><span class="pg">8</span></li>
    <li>COMPARABLE SALES DATA<span class="dots"></span><span class="pg">10</span></li>
    <li>PLANNING INFORMATION<span class="dots"></span><span class="pg">13</span></li>
    <li>TESTIMONIALS<span class="dots"></span><span class="pg">16</span></li>
    <li>WHO ARE YOU?<span class="dots"></span><span class="pg">16</span></li>
    <li>CONTACT<span class="dots"></span><span class="pg">20</span></li>
  </ul>
  <footer class="page-foot"><span class="num">3</span></footer>
</section>

<!-- Page 4: proposal -->
<section class="page p4">
  <header class="header-strip"><span class="left">PHONE NUMBER</span><span class="right">TRADING NAME</span></header>
  <h2 class="section-title">PROPOSAL</h2>
  <div class="title-bar" style="left:188px;top:58px"></div>
  <div class="photo" role="img" aria-label="Photo of hands on a laptop beside architectural floor plans" style="left:0;top:98px;width:322px;height:168px;background:linear-gradient(135deg,#d9dbdf,#f3f3f3 45%,#b8bcc4 70%,#e6e6e8)"></div>
  <h3 class="abs sub-head" style="left:37px;top:292px">Project Goal:</h3>
  <p class="abs body-small" style="left:37px;top:320px;width:280px">Purchase an existing house on a block of land, obtain development approval to demolish existing house and build two townhouses (dual occupancy side by side)</p>
  <h3 class="abs sub-head" style="left:37px;top:358px">Project Outcomes:</h3>
  <p class="abs body-small" style="left:37px;top:386px">Project Type: 2 Townhouse Development<br>Total Project Costs: $1,900,000<br>Total Cash/Equity Required: $627,991<br>Indicative Project Net Profit: $250,093<br>Indicative Project Return: 40%</p>
  <footer class="page-foot"><span class="num">4</span></footer>
</section>

<!-- Page 5: project location -->
<section class="page p5">
  <header class="header-strip"><span class="left">CREATIVITY AGENCY</span><span class="right">PROPOSAL</span></header>
  <h2 class="section-title" style="top:56px">PROJECT LOCATION</h2>
  <div class="title-bar" style="left:296px;top:60px"></div>
  <div class="photo" role="img" aria-label="Street map showing the route from the city centre to the project site" style="left:30px;top:102px;width:292px;height:170px;background:linear-gradient(120deg,#a9d4f0 0%,#c8e2ee 22%,#eeeadd 38%,#f1ecd8 100%)"></div>
  <div class="abs chip" style="top:288px">Station : 1.4 KM</div>
  <div class="abs chip" style="top:311px">Freeway Access: 1.5 KM</div>
  <div class="abs chip" style="top:334px">Shopping Centre: 1 KM</div>
  <div class="photo" role="img" aria-label="Photo of a freeway lined with trees near the suburb" style="left:30px;top:359px;width:119px;height:91px;background:linear-gradient(180deg,#bfd6e6 0%,#8fa07a 35%,#6f6f6a 65%,#9a9a94 100%)"></div>
  <h3 class="abs overview-head">OVERVIEW</h3>
  <p class="abs overview-lead">Include a brief description of the suburb.</p>
  <p class="abs overview-text">Leafy and chosen as most livable suburb in Melbourne on many occasions. Has good mix of primary and secondary schools. Family friendly with growing demographic</p>
  <footer class="page-foot"><span class="num">5</span></footer>
</section>

<!-- Page 6: photos -->
<section class="page p6">
  <header class="header-strip"><span class="left">PHONE NUMBER</span><span class="right">TRADING NAME</span></header>
  <h2 class="section-title">PHOTOS</h2>
  <div class="title-bar" style="left:161px;top:57px"></div>
  <div class="photo framed" role="img" aria-label="Before photo of the existing single-storey house" style="left:29px;top:90px;width:126px;height:70px;background:linear-gradient(180deg,#4e7fc9 0%,#9fc0e6 40%,#e7e2d7 60%,#6f8f4f 100%)"></div>
  <div class="abs tab" style="left:155px;top:99px;width:20px;height:51px"><span>Before</span></div>
  <svg class="abs" style="left:33px;top:188px" width="8" height="10" viewBox="0 0 24 30"><path d="M12 1C6 1 2 5.5 2 11c0 7 10 18 10 18s10-11 10-18C22 5.5 18 1 12 1z" fill="none" stroke="#f7923e" stroke-width="2.5"/><circle cx="12" cy="11" r="3.5" fill="#f7923e"/></svg>
  <p class="abs pin-text">Lorem ipsum road, city<br>code123456 Lorem ipsum</p>
  <div class="abs tab" style="left:178px;top:167px;width:20px;height:51px"><span>After</span></div>
  <div class="photo framed" role="img" aria-label="After render of the two new double-storey townhouses" style="left:198px;top:158px;width:124px;height:70px;background:linear-gradient(180deg,#4d86d6 0%,#a8c7ea 35%,#8a8580 60%,#3f3a35 100%)"></div>
  <div class="photo" role="img" aria-label="Aerial photo of the suburb around the site" style="left:55px;top:246px;width:267px;height:154px;background:linear-gradient(135deg,#7d7a6e,#9c9580 40%,#6e7560 70%,#8c8676)"></div>
  <div class="abs map-tag" style="left:257px;top:253px;width:48px">Hospital</div>
  <div class="abs map-tag" style="left:166px;top:282px;width:58px">Supermarket,<br>Café</div>
  <div class="abs map-tag" style="left:245px;top:314px;width:69px">Primary school</div>
  <div class="abs vertical-label">FEASIBILITY REPORT</div>
  <div class="abs costs-head">Acquisition and <em>Build Costs</em></div>
  <table class="abs costs">
    <tr><th style="width:94px"></th><th>Amount</th><th style="width:71px">Finance</th></tr>
    <tr><td>Land Purchase</td><td>$890,000</td><td>80% Residential</td></tr>
    <tr><td>Legal Fees</td><td>$1500</td><td></td></tr>
  </table>
  <footer class="page-foot"><span class="num">6</span></footer>
</section>

</body>
</html>
```